Kindling Haven of Alabama

We are a disaster relief nonprofit organization that provides relief to families children and pets when a disaster strikes multifamily. We need a easy and powerful piece that tells what we do and draws folks into finding out more. So a piece that could be used at tradeshows or speaking engagements
Updates

Be sure to include our social and other contact info. Added Monday, October 16, 2017

Target Market(s)

Potential Donors & Volunteers

Industry/Entity Type

Non-Profit

Font styles to use
Serif

Colors

Designer to choose colors to be used in the design.

Requirements
Must have
• Our logo and trigger photos I am going to rely on your expertise to create something compelling that is simple and powerful
Nice to have
• Moving pull on the heart strings

```html
<!DOCTYPE html>
<html lang="en">
<head>
<meta charset="utf-8">
<title>Kindling Haven of Alabama – Flyer</title>
<link href="https://fonts.googleapis.com/css2?family=Lato:wght@300;400;700&family=Tinos&display=swap" rel="stylesheet">
<style>
  :root {
    --bg: #e4e2df;
    --paper: #f4f3f1;
    --white: #ffffff;
    --band: #8e8d8c;
    --text: #454545;
    --muted: #707070;
    --accent: #f2a93b;
    --logo-gray: #8a8a8a;
  }
  * { box-sizing: border-box; margin: 0; padding: 0; }
  html, body { width: 1200px; height: 882px; overflow: hidden; }
  body { background: var(--bg); font-family: "Lato", sans-serif; color: var(--text); position: relative; }

  .card { position: absolute; top: 80px; width: 516px; height: 714px; background: var(--paper); box-shadow: 0 3px 10px rgba(0,0,0,.25); overflow: hidden; }
  .card--front { left: 48px; }
  .card--back { left: 618px; }

  /* front */
  .hero-photo { position: absolute; left: 0; top: 0; width: 100%; height: 458px;
    background:
      radial-gradient(ellipse 32% 40% at 52% 40%, rgba(70,66,66,.75), rgba(70,66,66,0) 100%),
      radial-gradient(ellipse 22% 18% at 46% 58%, rgba(196,150,112,.85), rgba(196,150,112,0) 100%),
      radial-gradient(ellipse 30% 22% at 40% 22%, rgba(110,104,100,.8), rgba(110,104,100,0) 100%),
      radial-gradient(ellipse 40% 50% at 14% 35%, rgba(250,250,248,.95), rgba(250,250,248,0) 100%),
      radial-gradient(ellipse 40% 45% at 86% 38%, rgba(246,245,243,.95), rgba(246,245,243,0) 100%),
      linear-gradient(180deg, #c7c1ba 0%, #e2ded9 45%, #b7b3ae 80%, #8f8c89 100%); }
  .badge { position: absolute; border-radius: 50%; border: 3px solid var(--accent); background: var(--white); }
  .badge--photo-left { left: 33px; top: 402px; width: 124px; height: 124px;
    background:
      radial-gradient(circle at 65% 60%, rgba(230,190,160,.95), rgba(230,190,160,0) 40%),
      radial-gradient(circle at 32% 45%, rgba(214,160,130,.95), rgba(214,160,130,0) 42%),
      linear-gradient(160deg, #f1c9cf 0%, #e9b8a0 50%, #a68a6e 100%); }
  .badge--photo-right { left: 357px; top: 402px; width: 124px; height: 124px;
    background:
      radial-gradient(circle at 30% 45%, rgba(92,58,40,.95), rgba(92,58,40,0) 38%),
      radial-gradient(circle at 55% 80%, rgba(230,196,110,.95), rgba(230,196,110,0) 35%),
      radial-gradient(circle at 72% 30%, rgba(170,40,40,.7), rgba(170,40,40,0) 30%),
      linear-gradient(150deg, #8a8a88 0%, #3a3230 55%, #2a2624 100%); }
  .badge--logo { left: 190px; top: 392px; width: 144px; height: 144px; display: flex; flex-direction: column; align-items: center; justify-content: center; }
  .logo-name { font-family: "Lato", sans-serif; font-weight: 300; color: var(--logo-gray); font-size: 24px; line-height: 1.05; text-align: center; }
  .logo-name small { display: block; font-size: 10px; }

  .intro { position: absolute; left: 19px; right: 20px; top: 555px; font-size: 13px; line-height: 16.4px; text-align: justify; color: var(--text); }
  .footer-band { position: absolute; left: 0; bottom: 0; width: 100%; height: 56px; background: var(--band); display: flex; align-items: center; padding-left: 18px; }
  .social { display: flex; gap: 4px; }
  .social span { width: 27px; height: 27px; border-radius: 50%; background: var(--white); display: block; }
  .site-url { margin-left: 42px; color: var(--white); font-weight: 700; font-size: 15px; letter-spacing: .2px; }

  /* back */
  .kit-photo { position: absolute; left: 0; top: 0; width: 100%; height: 232px;
    background:
      radial-gradient(ellipse 22% 30% at 78% 55%, rgba(248,248,246,.95), rgba(248,248,246,0) 100%),
      radial-gradient(ellipse 14% 14% at 82% 22%, rgba(214,170,140,.9), rgba(214,170,140,0) 100%),
      radial-gradient(ellipse 28% 40% at 42% 65%, rgba(205,160,96,.95), rgba(205,160,96,0) 100%),
      radial-gradient(ellipse 18% 22% at 28% 45%, rgba(220,220,222,.85), rgba(220,220,222,0) 100%),
      radial-gradient(ellipse 12% 60% at 3% 40%, rgba(96,130,70,.95), rgba(96,130,70,0) 100%),
      linear-gradient(180deg, #2a2d33 0%, #3b3f46 60%, #5b5e62 100%); }
  .list-title { position: absolute; top: 250px; width: 100%; text-align: center; font-family: "Tinos", serif; font-weight: 400; color: var(--accent); font-size: 22px; letter-spacing: .6px; }
  .item { position: absolute; padding-left: 24px; }
  .item--l { left: 18px; width: 230px; }
  .item--r { left: 266px; width: 232px; }
  .item svg { position: absolute; left: 0; top: 0; width: 17px; height: 17px; }
  .item h3 { font-weight: 400; font-size: 13px; color: var(--text); line-height: 17px; }
  .item h3 small { font-size: 9.5px; }
  .item p { font-size: 11px; line-height: 13.7px; color: var(--muted); text-align: justify; margin-top: 2px; }
  .mission-band { position: absolute; left: 0; top: 550px; width: 100%; height: 94px; background: var(--band); color: var(--white); font-size: 15px; line-height: 20px; text-align: center; padding: 15px 18px 0; }
  .partners { position: absolute; left: 0; top: 644px; width: 100%; height: 70px; display: flex; align-items: center; justify-content: space-evenly; padding: 0 20px; }
  .partners span { display: block; height: 20px; width: 60px; background: #b9bfc9; border-radius: 2px; }
  .partners span:nth-child(2n) { background: #8fa3c4; }
</style>
</head>
<body>
  <section class="card card--front">
    <div class="hero-photo" role="img" aria-label="Young child in a knit cap smiling and hugging a teddy bear on a bed with white pillows"></div>
    <div class="badge badge--photo-left" role="img" aria-label="Portrait of the co-founders, a mother and her son"></div>
    <div class="badge badge--logo">
      <div class="logo-name">Kindling<br>Haven<small>of Alabama</small></div>
    </div>
    <div class="badge badge--photo-right" role="img" aria-label="Smiling girl holding a teddy bear from a relief kit"></div>
    <p class="intro">Kindling Haven of Alabama was Co-Funded by Mara Lowell-Pierce and her son Declan Pierce to offer support to Residents that have been displaced from Apartment Homes due to fire or other disasters. Often times, displaces residents are placed in vacant apartment homes or even find themselves on the floor of the clubhouse util a plan is devised for next steps.</p>
    <div class="footer-band">
      <div class="social"><span></span><span></span><span></span></div>
      <div class="site-url">www.kindlinghavenofalabama.org</div>
    </div>
  </section>

  <section class="card card--back">
    <div class="kit-photo" role="img" aria-label="Boy leaning on boxed relief kits with a teddy bear in the back of a car"></div>
    <h2 class="list-title">DISASTER RELIEF KIT SUPPLY LIST</h2>

    <svg width="0" height="0" style="position:absolute">
      <symbol id="tick" viewBox="0 0 20 20"><circle cx="10" cy="10" r="8.5" fill="none" stroke="#f2a93b" stroke-width="1.6"/><path d="M6 10.2l3 3 5-6" fill="none" stroke="#f2a93b" stroke-width="1.8" stroke-linecap="round" stroke-linejoin="round"/></symbol>
    </svg>

    <div class="item item--l" style="top:291px"><svg><use href="#tick"/></svg><h3>Twin Air Mattress <small>(8.00 at ShopMart)</small></h3>
      <p>On almost all occasions, property management will place a resident into a vacant apartment. Our disaster relief kits give them everything that victims of disaster need to take refuge for the first few nights. Most often our kits are all that these families have.</p></div>
    <div class="item item--l" style="top:425px"><svg><use href="#tick"/></svg><h3>Standard Pillows <small>(2.37 at ShopMart)</small></h3></div>
    <div class="item item--l" style="top:457px"><svg><use href="#tick"/></svg><h3>Air Pumps <small>(13.00 ShopMart)</small></h3></div>
    <div class="item item--l" style="top:485px"><svg><use href="#tick"/></svg><h3>Blankets/Throws <small>(2.88 at ShopMart)</small></h3>
      <p>Small rolled fleece throws. We also take handmade items/must be new.</p></div>

    <div class="item item--r" style="top:291px"><svg><use href="#tick"/></svg><h3>Towels/Washcloths/Flat Sheets</h3></div>
    <div class="item item--r" style="top:317px"><svg><use href="#tick"/></svg><h3>Flip Flops- Solid Colors-All sizes<br><small>(ShopMart $1)</small></h3>
      <p>Most often victims of disaster are not wearing shoes due to the rushed escape, etc. We provide them with flip flops on scene.</p></div>
    <div class="item item--r" style="top:413px"><svg><use href="#tick"/></svg><h3>Penny Market Items All $1</h3>
      <p>Brush/Comb Combo, Toothbrush/Paste Travel Combo, Wipes, Deodorant, Hand Sanitizer, Soap, Shampoo, Conditioner. We prefer travel sized to ensure that it fits into our boxes and does not leak.</p></div>
    <div class="item item--r" style="top:512px"><svg><use href="#tick"/></svg><h3>Cases of Bottled Water</h3></div>

    <div class="mission-band">Kindling Haven of Alabama is a Birmingham, Alabama based 501c3 nonprofit organization that provides disaster relief to Residents displaced from Apartment Homes across the state of Alabama.</div>
    <div class="partners" aria-label="Partner associations">
      <span></span><span></span><span></span><span></span><span></span><span></span>
    </div>
  </section>
</body>
</html>
```